Construction Company - Aluminum Welding Substations - 8 page Brochure

See attached for very rough idea of brochure idea and general idea - primary goal is to highlight various services provided as unique for our industry.

- About Us - see website (brevoforge.com) & Company Resume

- Why Welded Fittings - see PPT & language in comments

- Services Provided - See categories broke out on website - highlight Aluminum Bus Welding, Bus Bending, All Weather Welding, Field Fabrication.

- Contact Page - see website

- Want to use as many photo's to highlight work as possible as people like to see the finished product of the substation/bus bending
Updates

Target Market(s)

General Contractors - we are Specialty Subcontractor

Industry/Entity Type

Construction - Welding Substations

Font styles to use
Serif
Sans Serif

Colors
0054AA
0677BA
7BADD7
CADEEF
E8F1F8
0094D4
00A9DD
6FCCEA
C7EBF8
E9F6FB
F0912C
F2A743
F7CA91
FBE8D2
FDF5EE

Requirements
Must have
• Logo, "Quality Craftsmanship without Compromise", Services Provided, as many pictures as makes sense to highlight work

```html
<!DOCTYPE html>
<html lang="en">
<head>
<meta charset="utf-8">
<title>Brevo Forge Industrial Welding – Brochure Spreads</title>
<link rel="stylesheet" href="https://fonts.googleapis.com/css2?family=Poppins:wght@400;500;600;700;800&display=swap">
<style>
:root{
  --stage:#8a8a8a;
  --navy:#17224a;
  --navy-2:#1f2f5e;
  --coral:#f4705c;
  --teal:#4ab5c9;
  --cyan:#5ec6d8;
  --ink:#1d2240;
  --rule:#c9ccd6;
  --white:#ffffff;
  --strip:#d9d9d9;
}
*{margin:0;padding:0;box-sizing:border-box}
html,body{width:1200px;height:2808px;overflow:hidden;background:var(--stage)}
body{position:relative;font-family:"Poppins",sans-serif;color:var(--ink)}
.page{position:absolute;width:452px;height:583px;overflow:hidden;background:var(--white);box-shadow:0 8px 16px rgba(0,0,0,.35)}
.abs{position:absolute}
.photo{position:absolute;background:linear-gradient(180deg,#6f9fd3 0%,#a9c6e3 55%,#8d8f8f 100%)}
.photo.inflow{position:relative}
.photo.dark{background:linear-gradient(160deg,#2b3f63 0%,#4c6b8e 60%,#3b3b3b 100%)}
.photo.spark{background:linear-gradient(160deg,#6c95c4 0%,#b9c8d4 45%,#d79b4b 70%,#4a5a5a 100%)}
.photo.shop{background:linear-gradient(180deg,#9aa0a6 0%,#c4c7ca 55%,#6f757b 100%)}
.photo.framed{border:2px solid var(--white)}

/* brand lettering */
.brand{position:absolute;left:0;right:0;text-align:center;color:var(--white);font-weight:600;line-height:1.1}
.brand .name{display:block;font-size:26px;letter-spacing:.5px}
.brand .sub{display:block;font-size:13px}

/* cover */
.cover{background:linear-gradient(180deg,#22356a 0%,var(--navy) 60%)}
.headline{position:absolute;left:0;right:0;text-align:center;font-weight:700;line-height:1.05}
.headline .l1{display:block;color:var(--cyan);font-size:27px}
.headline .l2{display:block;color:var(--white);font-size:27px}
.headline .thin{font-weight:400}
.tagline{position:absolute;left:82px;top:505px;height:18px;width:290px;border:1px solid var(--white);border-radius:10px;color:var(--white);font-size:9px;line-height:16px;padding-left:10px}
.tagline .pill{position:absolute;right:-1px;top:-1px;height:18px;line-height:18px;background:var(--coral);border-radius:10px;padding:0 10px;font-weight:600}
.url{position:absolute;left:0;right:0;text-align:center;font-size:10px;font-weight:600;letter-spacing:3px;color:var(--white)}
.url b{color:var(--coral);font-weight:600}

/* back cover */
.back{background:var(--navy)}
.call{position:absolute;left:0;right:0;top:418px;text-align:center;color:var(--coral);font-size:8.5px;font-weight:700;line-height:1.25}
.contacts{position:absolute;left:40px;top:462px;width:372px;display:flex}
.contacts .col{flex:1;padding:0 6px;font-size:6px;color:var(--white);line-height:1.9}
.contacts .col+.col{border-left:1px solid rgba(255,255,255,.5)}
.contacts h4{color:var(--teal);font-size:6.6px;font-weight:700;margin-bottom:3px}
.dot{display:inline-block;width:5px;height:5px;border-radius:50%;background:var(--coral);margin-right:4px;vertical-align:middle}

/* shared text */
.h-sec{font-weight:700;color:var(--teal);font-size:11.5px;line-height:1.3}
.h-coral{font-weight:700;color:var(--coral);font-size:9px}
.body{font-size:6.2px;line-height:1.35}
.checks{list-style:none;font-size:6.2px;line-height:1.35}
.checks li{position:relative;padding-left:10px;margin-bottom:2.5px}
.checks li::before{content:"";position:absolute;left:0;top:1px;width:6px;height:6px;border-radius:50%;background:var(--teal)}
.checks li::after{content:"";position:absolute;left:1.8px;top:2.3px;width:1.6px;height:2.6px;border:solid var(--white);border-width:0 1px 1px 0;transform:rotate(45deg)}
.checks.coral li::before,.checks li.coral-dot::before{background:var(--coral)}
.checks.white li::before{background:var(--white)}
.checks.white li::after{border-color:var(--coral)}
.checks .sub{margin-left:10px}
.hl-t{color:var(--teal);font-weight:700}
.hl-c{color:var(--coral);font-weight:700}
.bold{font-weight:700}
.on-navy{color:var(--white)}

/* about */
.about-strip{position:absolute;left:0;top:0;width:94px;height:583px;background:var(--white);overflow:hidden}
.about-word{position:absolute;left:4px;top:0;height:583px;writing-mode:vertical-rl;transform:rotate(180deg);font-size:96px;font-weight:800;color:var(--strip);line-height:86px;letter-spacing:-2px;text-align:center}
.about-panel{position:absolute;left:94px;top:0;width:358px;height:583px;background:var(--navy)}
.about-col{position:absolute;left:130px;top:36px;width:284px;color:var(--white)}
.pill-coral{display:inline-block;background:var(--coral);color:var(--white);font-size:6.8px;line-height:11px;border-radius:8px;padding:0 8px;margin:4px 0 6px}
.values{list-style:none;margin:8px 0 14px}
.value{display:flex;align-items:center;gap:12px;height:26px;margin-bottom:5px}
.value .ring{position:relative;flex:0 0 26px;width:26px;height:26px;border-radius:50%;border:2.5px solid var(--coral);background:var(--navy-2)}
.value .ring::after{content:"";position:absolute;left:6px;top:6px;width:9px;height:9px;border-radius:50%;background:var(--cyan)}
.value .t{font-size:6.4px;line-height:1.5}
.value .t b{display:block;font-weight:700}

/* footer */
.footer{position:absolute;left:0;top:536px;width:452px;height:14px}
.footer .bar{position:absolute;left:0;top:0;width:177px;height:13px;background:var(--coral);color:var(--white);font-size:6.5px;font-weight:600;letter-spacing:2.5px;line-height:13px;padding-left:40px}
.footer .line{position:absolute;left:181px;top:6px;width:214px;height:1px;background:var(--rule)}
.footer .num{position:absolute;left:395px;top:-1px;width:16px;height:16px;border-radius:50%;border:1.5px solid var(--teal);color:var(--teal);font-size:7px;font-weight:700;text-align:center;line-height:13px}

/* boxes */
.box-navy{position:absolute;background:var(--navy);color:var(--white);padding:12px 14px}
.box-coral{position:absolute;background:var(--coral);color:var(--white);padding:12px 14px}
.box-title{font-weight:700;font-size:8.5px;margin-bottom:5px}
.box-navy .box-title{color:var(--coral)}

/* services */
.svc-title{position:absolute;left:40px;top:38px;font-size:20px;font-weight:700;color:var(--coral)}
.svc{position:absolute}
.svc .n{position:absolute;left:0;top:0;width:22px;height:22px;border-radius:50%;background:var(--navy);border:2px solid var(--white);box-shadow:0 0 0 1.5px var(--coral);color:var(--white);font-size:8px;font-weight:700;text-align:center;line-height:18px}
.svc .stem{position:absolute;left:10px;top:24px;width:1px;background:var(--rule)}
.svc h3{position:absolute;left:33px;top:2px;font-size:13px;font-weight:700;color:var(--navy);white-space:nowrap}
.svc .what{position:absolute;left:33px;top:21px;font-size:8px;font-weight:700;color:var(--teal);white-space:nowrap}
.svc .what.wrap{white-space:normal;line-height:1.2}
.svc ul{position:absolute;left:33px;top:35px}
</style>
</head>
<body>

<!-- PAGE 1 · FRONT COVER -->
<section class="page cover" style="left:117px;top:145px">
  <div class="brand" style="top:58px"><span class="name">Brevo Forge</span><span class="sub">Industrial Welding, Inc.</span></div>
  <div class="photo framed" style="left:76px;top:145px;width:146px;height:113px" role="img" aria-label="Welder on an orange aerial lift working on substation bus"></div>
  <div class="photo framed dark" style="left:76px;top:265px;width:146px;height:103px" role="img" aria-label="Substation steel structures and bus against blue sky"></div>
  <div class="photo framed spark" style="left:228px;top:145px;width:147px;height:223px" role="img" aria-label="Welder grinding an aluminum pipe with sparks flying"></div>
  <div class="headline" style="top:405px">
    <span class="l1">QUALITY</span>
    <span class="l1">CRAFTSMANSHIP</span>
    <span class="l2"><span class="thin">WITHOUT</span> COMPROMISE</span>
  </div>
  <div class="tagline">Leaders in the welding industry for <span class="pill">over 25 years</span></div>
  <div class="url" style="top:535px">www.<b>brevoforge</b>.com</div>
</section>

<!-- PAGE 2 · BACK COVER -->
<section class="page back" style="left:632px;top:145px">
  <div class="photo dark" style="left:0;top:0;width:452px;height:400px;opacity:.55;background:linear-gradient(180deg,#1b2b55 0%,#2a3f6b 55%,var(--navy) 100%)" role="img" aria-label="Dimmed substation silhouette at dusk"></div>
  <div class="brand" style="top:252px"><span class="name">Brevo Forge</span><span class="sub">Industrial Welding, Inc.</span></div>
  <div class="call">CALL FOR AN APPOINTMENT TO DISCUSS<br>YOUR WELDING NEEDS<br><span style="color:var(--white);letter-spacing:1px">••••••</span></div>
  <div class="contacts">
    <div class="col"><h4>Office/Regular Business Hours</h4><span class="dot"></span>555-210-4837<br>Marla Brevo, President<br>Curtis Brevo, Vice President</div>
    <div class="col"><h4>After Hours/Emergencies</h4><span class="dot"></span>555-318-6642<br>Dale Hollis, Foreman<br>Reid Calder, Foreman</div>
    <div class="col"><h4>Mailing Address</h4>Brevo Forge Industrial<br><span class="dot"></span>P.O. Box 40218<br><span class="dot"></span>Cedar Falls, WA 98714</div>
  </div>
  <div class="url" style="top:535px">www.<b>brevoforge</b>.com</div>
</section>

<!-- PAGE 3 · ABOUT US -->
<section class="page" style="left:117px;top:787px">
  <div class="about-strip"><div class="about-word">ABOUT US</div></div>
  <div class="about-panel"></div>
  <div class="about-col">
    <div class="h-sec">Family Owned Business</div>
    <span class="pill-coral">Trusted since incorporation in <b>1997</b></span>
    <p class="body">We are an organization built on integrity. As a privately owned company, the commitment to our core values starts with our leadership and runs through our entire organization.</p>
    <div class="h-sec" style="margin-top:10px">What We Believe</div>
    <ul class="values">
      <li class="value"><span class="ring"></span><span class="t"><b>Safety</b>Our work is never more important than our people and the people around us</span></li>
      <li class="value"><span class="ring"></span><span class="t"><b>Integrity</b>Consistently doing the right thing when no one is looking</span></li>
      <li class="value"><span class="ring"></span><span class="t"><b>Innovation</b>Problem solving through expertise and creativity</span></li>
      <li class="value"><span class="ring"></span><span class="t"><b>Respect</b>Treating others as you would want to be treated</span></li>
      <li class="value"><span class="ring"></span><span class="t"><b>Teamwork</b>Working together to provide a quality customer experience</span></li>
    </ul>
    <div class="photo inflow" style="width:282px;height:116px" role="img" aria-label="Wide view of a completed substation with aluminum bus and steel structures"></div>
    <div class="h-sec" style="margin-top:10px">Company Background</div>
    <p class="body" style="margin-top:4px;font-size:5.9px">Brevo Forge Industrial Welding, Inc.'s (BFI) mission is to provide quality craftsmanship without compromise. We are an organization built on integrity where the commitment to our core values starts with our leadership and runs throughout our entire organization. We value the safety of our employees through the implementation of a rigorous safety training program which has protected our employees throughout our 27+ years in operation. BFI emphasizes the continued growth of our employees through hands-on, on-the-job training to expand both our employees' professional and technical skill sets. Our employees take pride in extending excellent customer service to every customer by providing innovative solutions to complex problems through integrity, respect, and teamwork.</p>
  </div>
</section>

<!-- PAGE 4 · WHY WELDED CONNECTORS -->
<section class="page" style="left:632px;top:787px">
  <div class="abs" style="left:0;top:0;width:270px;height:157px;background:var(--teal)"></div>
  <div class="abs" style="left:40px;top:38px;font-size:13px;font-weight:700;color:var(--navy)">Why Welded Connectors?</div>
  <div class="abs hl-c" style="left:40px;top:58px;font-size:7px">IESC – PREFERRED METHOD</div>
  <ul class="checks coral abs" style="left:40px;top:71px;width:222px;color:var(--navy)">
    <li>Per IESC 6.6.1.4, Welded connectors are the preferred method of bus and cable installation in power substations.</li>
    <li>Per IESC 6.6.1.2 Compression fittings are intended to be installed on <b>stranded conductors</b>. Compressed should be oriented down to prevent the entrance of moisture into the connection.</li>
  </ul>
  <div class="photo" style="left:270px;top:0;width:182px;height:157px" role="img" aria-label="Lineman on a lift welding overhead bus connections"></div>

  <div class="abs" style="left:0;top:157px;width:452px;height:139px;background:var(--navy)"></div>
  <div class="abs h-coral" style="left:40px;top:172px">RELIABILITY/LOW RESISTANCE</div>
  <ul class="checks abs on-navy" style="left:40px;top:187px;width:375px">
    <li>Forms a <span class="hl-t">SOLID</span>, homogeneous connection.</li>
    <li>Excellent structural, mechanical and electrical performance with <span class="hl-t">NO CONTACT RESISTANCE (IESC)</span></li>
    <li>Northridge Power Authority did a study on welded substations and connectors and found that in the case of a seismic event welding creates a <span class="hl-t">SEISMICLY SUPERIOR</span> overall substation, when welded properly.</li>
    <li>No risk of <span class="hl-t">EXPANSION OR CONTRACTION</span></li>
    <li><span class="hl-t">LESS CHANCE OF CORONA</span> in high voltage EHV and UHV applications – keeping the profile smooth.</li>
  </ul>

  <div class="abs h-coral" style="left:40px;top:312px">ADAPTABILITY/AVAILABILITY</div>
  <ul class="checks coral abs" style="left:40px;top:328px;width:375px">
    <li><b>Ability to <span class="hl-c">REUSE EXISTING PARTS</span></b> – no down time of having to wait on replacement parts.</li>
    <li><b>Ability to <span class="hl-c">MODIFY NEW OR EXISTING PARTS</span></b> – adapt to special circumstances in real time.</li>
    <li><b>Ability to perform <span class="hl-c">ONSITE FIELD MODIFICATIONS</span> such as:</b></li>
    <li class="sub">Retro Fitting Motor Operating Disconnects (MOD's)</li>
    <li class="sub">Elevation changes with new equipment</li>
    <li class="sub">Needing to modify connectors to maintain proper alignment</li>
  </ul>
  <div class="photo" style="left:40px;top:419px;width:137px;height:87px" role="img" aria-label="Substation yard with service trucks and stacked aluminum bus"></div>
  <div class="box-coral" style="left:180px;top:419px;width:231px;height:87px">
    <div class="box-title">CLEAN AESTHETICS</div>
    <ul class="checks white"><li>No sharp edges</li><li>No scarring of outer surfaces on the bus.</li><li>Clean Lines – when bus bending utilized</li><li>Greater customer satisfaction with finished product</li></ul>
  </div>
  <div class="footer"><div class="bar">www.brevoforge.com</div><div class="line"></div><div class="num">2</div></div>
</section>

<!-- PAGE 5 · COMMON CONCERNS -->
<section class="page" style="left:117px;top:1426px">
  <div class="abs" style="left:0;top:0;width:308px;height:213px;background:var(--navy)"></div>
  <div class="abs h-sec" style="left:40px;top:37px;font-size:12px">Common Concerns</div>
  <ul class="checks abs on-navy" style="left:40px;top:58px;width:260px">
    <li class="bold">All BFI Welders are</li>
    <li class="sub coral-dot">WCB-certified for both steel and <span class="hl-t">aluminum</span></li>
    <li class="sub coral-dot">NPA Certified for both MIG and TIG</li>
    <li class="bold">Directly trained in high voltage substations</li>
    <li><b>Perform In-house training –</b> high internal quality control standards.</li>
    <li><b>Niche/Specialty –</b> Perform this work everyday, creates inherent efficiencies.</li>
    <li class="bold">Currently have 11 fully outfitted welding trucks</li>
    <li class="bold">Currently licensed in 8 states</li>
    <li class="bold">Continuously expanding our work force and territory</li>
  </ul>
  <div class="photo spark" style="left:308px;top:0;width:144px;height:213px" role="img" aria-label="Gloved welder grinding an aluminum tube with sparks"></div>

  <div class="photo" style="left:40px;top:218px;width:137px;height:104px" role="img" aria-label="Substation at sunrise with a hill behind"></div>
  <div class="photo" style="left:40px;top:326px;width:137px;height:102px" role="img" aria-label="Crew on lift installing bus in a substation"></div>
  <div class="photo" style="left:40px;top:432px;width:137px;height:87px" role="img" aria-label="Completed substation bus structures"></div>

  <div class="abs h-coral" style="left:193px;top:225px">SAFETY/QUALITY/EFFICIENCY</div>
  <div class="abs" style="left:193px;top:247px;width:220px;font-size:6.2px;line-height:1.35">
    <div style="display:flex;margin-bottom:12px"><span class="hl-t" style="flex:0 0 45px">Safety</span><span style="flex:1">Never had a recordable Safety Incident – EMR Rating of .77</span></div>
    <div style="display:flex;margin-bottom:12px"><span class="hl-t" style="flex:0 0 45px">Quality</span><span style="flex:1"><span class="hl-t">Company Culture Emphasizes Quality –</span> its one of our core values<br><span class="hl-t">Company Moto:</span> "Quality Craftsmanship without Compromise"<br><span class="hl-t">Customer Satisfaction – Standard</span> = Every customer/every time</span></div>
    <div style="display:flex"><span class="hl-t" style="flex:0 0 45px">Efficiency</span><span style="flex:1"><span class="hl-t">One stop shop</span> – perform layout, cutting, fitting, prefab, arial installation, routing of bus, troubleshooting.<br><span class="hl-t">"Be part of the solution, not part of the problem"</span> – Core Value<br><span class="hl-t">No wasted movements</span> – everything we do has a purpose</span></div>
  </div>
  <div class="box-coral" style="left:180px;top:432px;width:231px;height:87px">
    <div class="box-title">WEATHER</div>
    <ul class="checks white"><li>Weather of any type can impact installation efficiency regardless of the application used.</li><li>Can be mitigated with the use of skilled, qualified and certified aluminum welders with experience in power substations.</li></ul>
  </div>
  <div class="footer"><div class="bar">www.brevoforge.com</div><div class="line"></div><div class="num">3</div></div>
</section>

<!-- PAGE 6 · SERVICES 1–2 -->
<section class="page" style="left:632px;top:1426px">
  <div class="svc-title">SERVICES</div>
  <div class="svc" style="left:40px;top:80px;width:236px;height:92px">
    <div class="n">1</div><div class="stem" style="height:70px"></div>
    <h3>All Weather Welding</h3>
    <div class="what wrap" style="width:180px">Types of weather we successfully perform quality welds in</div>
    <ul class="checks" style="top:47px;width:170px"><li>Rain</li><li>Snow</li><li>Wind</li><li>Warm and Cold Weather</li></ul>
  </div>
  <div class="photo" style="left:281px;top:41px;width:130px;height:130px" role="img" aria-label="Welder on a lift beside substation structures in winter"></div>
  <div class="photo shop" style="left:281px;top:177px;width:130px;height:89px" role="img" aria-label="Welder working beside insulators in the snow"></div>
  <div class="box-navy" style="left:40px;top:177px;width:238px;height:89px">
    <div class="box-title">Advantages</div>
    <ul class="checks coral"><li>Year around work</li><li>Ability to keep projects on schedule without delays or stoppage</li><li>Ability to adapt to all weather conditions</li></ul>
  </div>
  <div class="photo" style="left:40px;top:270px;width:129px;height:140px" role="img" aria-label="Crew on an orange lift welding elevated bus"></div>
  <div class="photo dark" style="left:40px;top:414px;width:129px;height:98px" role="img" aria-label="Close-up of a welder at work with glowing arc"></div>
  <div class="svc" style="left:187px;top:283px;width:224px;height:125px">
    <div class="n">2</div><div class="stem" style="height:95px"></div>
    <h3>Aluminum Welding</h3>
    <div class="what">What We Do</div>
    <ul class="checks" style="width:190px"><li>Metalic Inert Gas (MIG)</li><li>Tungsten Inert Gas (TIG)</li><li>Custom field fabrication</li><li>Shop fabrication</li></ul>
    <div class="abs hl-c" style="left:33px;top:96px;font-size:6.8px;white-space:nowrap">Other aluminum welding specialty services</div>
    <div class="abs bold" style="left:33px;top:108px;width:190px;font-size:6.2px;line-height:1.35">Bus Bending <span class="hl-c">|</span> Wire Jumpers <span class="hl-c">|</span> Switch Yards <span class="hl-c">|</span> Distribution Racks</div>
  </div>
  <div class="box-coral" style="left:172px;top:414px;width:239px;height:98px">
    <div class="box-title">Advantages</div>
    <ul class="checks white"><li>Fully bonded electrical connection</li><li>No maintenance due to bolted or compression connections</li><li>Cost effective with readily available parts</li><li>Smooth edges to reduce corona</li></ul>
  </div>
  <div class="footer"><div class="bar">www.brevoforge.com</div><div class="line"></div><div class="num">4</div></div>
</section>

<!-- PAGE 7 · SERVICES 3–4 -->
<section class="page" style="left:117px;top:2078px">
  <div class="svc-title">SERVICES</div>
  <div class="svc" style="left:40px;top:80px;width:236px;height:92px">
    <div class="n">3</div><div class="stem" style="height:70px"></div>
    <h3>Bus Bending</h3>
    <div class="what">What We Do</div>
    <ul class="checks" style="width:195px"><li>Ability to bend 1/2" to 5" bus</li><li>Calculate elevation and compound angles.</li><li>Design, bend and lay out as needed.</li><li>Calculate distances for phase to ground and phase to phase clearances.</li></ul>
  </div>
  <div class="photo" style="left:282px;top:41px;width:129px;height:130px" role="img" aria-label="Bent aluminum bus runs on substation structures"></div>
  <div class="photo dark" style="left:282px;top:175px;width:129px;height:115px" role="img" aria-label="Worker on lift installing bent bus overhead"></div>
  <div class="box-navy" style="left:40px;top:175px;width:238px;height:115px">
    <div class="box-title">Advantages</div>
    <ul class="checks coral"><li>Continuous bus run with smoother transition in elevations.</li><li>Fewer fittings required, for a cost savings on parts and labor.</li><li>Faster and easier assembly for a better quality finished product.</li><li>Less chance of corona</li></ul>
  </div>
  <div class="photo shop" style="left:40px;top:295px;width:130px;height:114px" role="img" aria-label="Fabricated aluminum cable wireway boot"></div>
  <div class="photo" style="left:40px;top:413px;width:130px;height:101px" role="img" aria-label="Substation crew with trucks and lifts on site"></div>
  <div class="svc" style="left:188px;top:314px;width:223px;height:95px">
    <div class="n">4</div><div class="stem" style="height:62px"></div>
    <h3>Field Fabrication</h3>
    <div class="what">What We Do</div>
    <ul class="checks" style="width:190px"><li>Custom fabricate cable wireway boots</li><li>Custom fabricate necessary parts when needed</li><li>Weld and install bus and fittings as per engineered drawings</li><li>Resolve problems as they arise</li></ul>
  </div>
  <div class="box-coral" style="left:175px;top:413px;width:236px;height:101px">
    <div class="box-title">Advantages</div>
    <ul class="checks white"><li>Ability to fabricate and assemble on site</li><li>Less downtime for outages</li><li>Adapt to changing field conditions</li><li>Field modifications as needed</li><li>More cost effective for our customers to be able to field modify on site</li></ul>
  </div>
  <div class="footer"><div class="bar">www.brevoforge.com</div><div class="line"></div><div class="num">5</div></div>
</section>

<!-- PAGE 8 · SERVICES 5–6 -->
<section class="page" style="left:632px;top:2078px">
  <div class="svc-title">SERVICES</div>
  <div class="svc" style="left:40px;top:80px;width:236px;height:115px">
    <div class="n">5</div><div class="stem" style="height:95px"></div>
    <h3>Shop Fabrication</h3>
    <div class="what">What We Do</div>
    <ul class="checks" style="width:195px"><li>Assemble a variety of substation parts and pieces</li><li>Prefabrication of substation parts for faster and easier assembly in the field including:</li><li class="sub coral-dot">Cable Wireway Boots</li><li class="sub coral-dot">Wire Jumpers</li><li class="sub coral-dot">Underground Cable Bus Connections</li></ul>
  </div>
  <div class="photo spark" style="left:281px;top:41px;width:130px;height:155px" role="img" aria-label="Welder fabricating parts in the shop"></div>
  <div class="photo shop" style="left:281px;top:200px;width:130px;height:90px" role="img" aria-label="Rows of prefabricated aluminum bus assemblies"></div>
  <div class="box-navy" style="left:40px;top:200px;width:238px;height:90px">
    <div class="box-title">Advantages</div>
    <ul class="checks coral"><li>Faster field assembly</li><li>Less downtime in the field</li><li>Cost savings for our customers</li><li>Built to customer designs and specifications</li></ul>
  </div>
  <div class="photo shop" style="left:40px;top:295px;width:129px;height:113px" role="img" aria-label="Large power transformer in a substation yard"></div>
  <div class="photo shop" style="left:40px;top:413px;width:129px;height:101px" role="img" aria-label="Fabricated steel bracket pieces on the ground"></div>
  <div class="svc" style="left:187px;top:314px;width:224px;height:95px">
    <div class="n">6</div><div class="stem" style="height:62px"></div>
    <h3>Steel Welding</h3>
    <div class="what">What We Do</div>
    <ul class="checks" style="width:190px"><li>Seismic tie-down of transformers</li><li>Transformer tap changer installation</li><li>Steel modification of yard structures when needed</li><li>Steel repair of existing structures</li></ul>
  </div>
  <div class="box-coral" style="left:172px;top:413px;width:239px;height:101px">
    <div class="box-title">Advantages</div>
    <ul class="checks white"><li>Ability to fabricate customer designs on site.</li><li>Modifications no longer need to be returned to the manufacturer.</li><li>Repairs can be done immediately on site.</li><li>Cost savings of time and labor</li><li>Reduction of downtime for the customer</li></ul>
  </div>
  <div class="footer"><div class="bar">www.brevoforge.com</div><div class="line"></div><div class="num">6</div></div>
</section>

</body>
</html>
```